Brochure Design Project for Home Watch company

We are a new start up company in fast growing home watch industry. We provide services in Hawaii so the design needs to be reflect that. Our web site can give you overview of what we do - www.palmcrestkeeper.com. We will service clients that own second homes in Hawaii. These properties are not necessarily income producing properties for our clients. I'm looking for 2 or 4 page brochure which will be used to market our services to potential new clients. It needs to be high quality, modern with slight Hawaiian feel (we are based on Oahu). I'm not looking for a trifold type of brochure.

We are open to various colors based on what the designer might suggest but as you can see on our home page - the main picture of the home on our site has lots of red and white which we like as well as the "head" or dot above the "i" in our logo is red. I was not able to upload the file of the main house (purchased on snapvaultpix) on here therefore I'll have to provide the original photo to the selected designer at the later time. For now I just uploaded the not purchased copy.

If you have other questions please do let me know. And lastly, I will be looking to create a business card and post card as well.

```html
<!DOCTYPE html>
<html lang="en">
<head>
<meta charset="utf-8">
<title>Palm Crest Keeper – Home Watch Brochure</title>
<link rel="stylesheet" href="https://fonts.googleapis.com/css2?family=Roboto:wght@300;400&family=Lato:wght@400;700&display=swap">
<style>
  :root {
    --red: #e8505b;
    --ink: #3a3a3a;
    --muted: #8a8a8a;
    --line: #d9d9d9;
    --icon-bg: #e6e6e6;
    --paper: #ffffff;
    --stage: #eeeeee;
  }
  * { box-sizing: border-box; margin: 0; padding: 0; }
  html, body { width: 1200px; height: 996px; overflow: hidden; }
  body {
    background: var(--stage);
    font-family: "Lato", Arial, sans-serif;
    color: var(--ink);
    display: flex; align-items: center; justify-content: center;
  }
  .spread { display: flex; width: 1120px; height: 792px; box-shadow: 0 10px 30px rgba(0,0,0,.12); }
  .page { position: relative; width: 560px; height: 792px; background: var(--paper); overflow: hidden; }
  .page--left { border-right: 1px solid #f0f0f0; }

  /* left page */
  .hero {
    position: absolute; left: 0; top: 0; width: 560px; height: 360px;
    background: linear-gradient(180deg, #33507e 0%, #4e6a8a 40%, #b07a3c 62%, #2f6f9a 80%, #1e4f7a 100%);
  }
  .hero-curve { position: absolute; left: 0; top: 220px; width: 560px; height: 140px; }
  .devices {
    position: absolute; left: 36px; top: 276px; width: 170px; height: 128px;
    background: linear-gradient(160deg, #4a4f56, #1f2328); border-radius: 6px;
  }
  .values { position: absolute; left: 30px; top: 446px; width: 180px; display: flex; flex-direction: column; gap: 32px; }
  .value { text-align: center; }
  .value-icon {
    width: 50px; height: 50px; border-radius: 50%; background: var(--icon-bg);
    margin: 0 auto 10px; display: flex; align-items: center; justify-content: center;
  }
  .value-label { font-size: 12px; line-height: 1.3; color: var(--ink); }

  .watch { position: absolute; left: 236px; top: 360px; width: 300px; }
  .watch-kicker { font-size: 10px; color: var(--muted); }
  .watch-title { font-family: "Roboto", sans-serif; font-weight: 300; font-size: 24px; color: var(--red); margin: 2px 0 14px; }
  .service { margin-bottom: 16px; }
  .service:last-child { margin-bottom: 0; }
  .service-title { font-family: "Roboto", sans-serif; font-weight: 300; font-size: 17px; margin-bottom: 4px; }
  .service-text { font-size: 10.5px; line-height: 1.42; text-align: justify; }

  /* right page */
  .concierge-title { position: absolute; top: 56px; left: 0; width: 560px; text-align: center;
    font-family: "Roboto", sans-serif; font-weight: 300; font-size: 24px; color: var(--red); }
  .columns { position: absolute; top: 104px; left: 44px; width: 472px; display: flex; gap: 28px; }
  .column { flex: 1; }
  .column-title { font-family: "Roboto", sans-serif; font-weight: 300; font-size: 16px; text-align: center; margin-bottom: 6px; }
  .column-text { font-size: 10px; line-height: 1.45; text-align: justify; }
  .special { position: absolute; top: 290px; left: 44px; width: 472px; }
  .special-title { font-family: "Roboto", sans-serif; font-weight: 300; font-size: 17px; text-align: center; margin-bottom: 6px; }
  .special-text { font-size: 10px; line-height: 1.45; text-align: justify; }

  .quote {
    position: absolute; left: 44px; top: 470px; width: 200px; height: 150px;
    border: 1px solid var(--line); border-radius: 10px; padding: 18px 20px;
    font-size: 12px; line-height: 1.45; text-align: center; color: var(--ink);
  }
  .quote-mark { color: var(--red); font-family: "Roboto", sans-serif; font-size: 22px; line-height: 0; vertical-align: -6px; margin-right: 4px; }
  .cutaway {
    position: absolute; left: 270px; top: 430px; width: 246px; height: 190px;
    background: linear-gradient(180deg, #f2f2f2, #d7d7d7); border-radius: 6px;
  }
  .footer-swoosh { position: absolute; left: 0; bottom: 0; width: 560px; height: 200px; }
  .site-url { position: absolute; right: 36px; bottom: 128px; font-size: 14px; color: var(--red); }
</style>
</head>
<body>
<main class="spread">
  <section class="page page--left">
    <div class="hero" role="img" aria-label="Hawaiian villa with lit lanai and pool at dusk beneath green mountains and palms"></div>
    <svg class="hero-curve" viewBox="0 0 560 140" preserveAspectRatio="none" aria-hidden="true">
      <path d="M0 140 L0 120 C180 80 380 50 560 10 L560 140 Z" fill="var(--red)"/>
      <path d="M0 140 L0 132 C190 96 390 64 560 24 L560 140 Z" fill="#fff"/>
    </svg>
    <div class="devices" role="img" aria-label="Laptop and tablet showing a home inspection checklist"></div>

    <div class="values">
      <div class="value">
        <div class="value-icon">
          <svg width="26" height="20" viewBox="0 0 26 20" aria-hidden="true"><path d="M2 8 L8 3 L13 6 L18 3 L24 8 L14 17 Z" fill="var(--red)"/></svg>
        </div>
        <p class="value-label">High moral and ethical values</p>
      </div>
      <div class="value">
        <div class="value-icon">
          <svg width="24" height="22" viewBox="0 0 24 22" aria-hidden="true"><path d="M12 21 C4 15 1 11 1 7 A5.5 5.5 0 0 1 12 4 A5.5 5.5 0 0 1 23 7 C23 11 20 15 12 21 Z" fill="var(--red)"/></svg>
        </div>
        <p class="value-label">Passionate and hardworking attitude</p>
      </div>
      <div class="value">
        <div class="value-icon">
          <svg width="24" height="24" viewBox="0 0 24 24" aria-hidden="true"><path d="M3 8 H9 A3 3 0 1 1 15 8 H21 V14 A3 3 0 1 0 21 20 V22 H3 Z" fill="var(--red)"/></svg>
        </div>
        <p class="value-label">Enhanced attention to details</p>
      </div>
    </div>

    <div class="watch">
      <p class="watch-kicker">Monthly, bi-weekly or weekly visual inspections</p>
      <h1 class="watch-title">Primary HOME WATCH</h1>
      <div class="service">
        <h2 class="service-title">General Outdoor Visual Inspections</h2>
        <p class="service-text">Check yard, lawn and landscaping; check lanai, deck, and pool area for any damage; check for mold or fading of all outdoor furniture; check water level of swimming pool or hot tub, if applicable</p>
      </div>
      <div class="service">
        <h2 class="service-title">Home Exterior Visual Inspections</h2>
        <p class="service-text">Check security cameras; check for overall damage; remove mail, newspapers, and flyers from mailbox and store inside of the property; check outdoor plumbing and hoses for leakage; check garage; check for vandalism and theft</p>
      </div>
      <div class="service">
        <h2 class="service-title">Home Interior Visual Inspections</h2>
        <p class="service-text">Make sure security system is in working order; ensure that all doors, windows and sliders are locked and secured; check thermostats and make sure the air conditioning is set at appropriate and requested temperature; make sure all smoke detectors are in proper working order or replace batteries if necessary; visually inspect the water heater and washer and dryer</p>
      </div>
    </div>
  </section>

  <section class="page page--right">
    <h1 class="concierge-title">Concierge Services</h1>
    <div class="columns">
      <div class="column">
        <h2 class="column-title">Pre-Arrival</h2>
        <p class="column-text">Groceries purchased and stored; air conditioning and ceiling vents turned on and/or windows opened; water turned on; fresh linens placed on beds; flowers placed in bathrooms; deck furniture placed on lanai and patio; house freshened up and aired out; security system disarmed as appropriate; decks, walkways, lanais and driveways cleaned of debris and special requests completed.</p>
      </div>
      <div class="column">
        <h2 class="column-title">Post-Departure</h2>
        <p class="column-text">House cleaning coordinated, beds made, sheets and towels cleaned, dishes washed and put away, all doors and windows secured, lights on timers set, water turned off, outdoor furniture stored or covered per specific instructions, driveways, lanais, walkways and decks cleared of debris, air conditioning set to appropriate level, trash placed for collection and security system turned on.</p>
      </div>
    </div>
    <div class="special">
      <h2 class="special-title">Sample of Special Services/Requests</h2>
      <p class="special-text">Key holding services, mail forwarding, coordination of transportation from and to the airport, light handyman and landscaping services, vendor coordination (we coordinate access and meet everyone you authorize at your home including but not limited to maintenance, repair, pest control, landscaping and tree trimming, and utility providers), pre-storm services (secure outdoor furniture, potted plants, hammocks and any other outdoor items, etc.) and post-storm services (clean walkway and driveway, pick-up trash, etc.), and emergency services response, etc. Additional services and pricing available upon request.</p>
    </div>

    <blockquote class="quote"><span class="quote-mark">&ldquo;</span>Don't let repairs or unexpected surprises upon your arrival take away from your vacation time. Arrive in Hawaii and simply enjoy your second home and the island.</blockquote>
    <div class="cutaway" role="img" aria-label="Cutaway illustration of a two-storey house with rooms and service icons around it"></div>

    <svg class="footer-swoosh" viewBox="0 0 560 200" preserveAspectRatio="none" aria-hidden="true">
      <path d="M40 200 C200 150 400 120 560 80 L560 100 C400 135 220 170 40 200 Z" fill="var(--red)"/>
    </svg>
    <p class="site-url">www.palmcrestkeeper.com</p>
  </section>
</main>
</body>
</html>
```